PowerPoint Design Project

Design Brief
Corvanta is updating its stationary templates to reflect the company’s position as market leader in smart-location based solutions.
Using the existing Corvanta logo and corporate colours, create an engaging and visually appealing PowerPoint presentation template identity that works when printed on A4 and US Letter sized paper.
The successful designs will complement the current look and feel of the Corvanta website (www.corvanta-example.net) and communicate that Corvanta is a dynamic and modern technology company that is at the cutting edge of innovation.
Corvanta Brand
Corvanta stands for Precision Location Technology. The brand represents both a unique, highly innovative platform product and a mature consulting and support organisation dedicated to delivering solutions to blue-chip customer problems. The orange colour implies creativity while blue evokes trust and a rational approach. “Cor” is Latin and means “where”, so the brand directly addresses the focus of the company: location. “Sense” can mean that we have sensing technology to support our precision location aware applications and solutions, but also that we make sensible use of location data to improve customer processes.
Corvanta Corporate Profile
Corvanta is a market leader of location-based Smart Factory Solutions which enables companies to optimise their business processes. By keeping track of key assets, Corvanta solutions bring clarity to complex operations in industries while also improving quality and reliability. Corvanta uses a unique combination of advancefd industry knowledge and an experienced team to deliver effective and superior solutions that offer unprecedented visibility, control and accuracy, delivering time and cost savings. Corvanta solutions are easy to implement and flexible to a particular business’s needs, no matter which area of the globe they operate in.
Corvanta offers two location-oriented products; RTLS (Real-time Location Solutions) and Geospatial Systems and operates in a number of industries ranging from manufacturing and utilities to telecommunications and is used by a number of blue chip customers across the world, such as KLT, Skyvane, Dromtrack, Pellow Power, RIM and Nordfeld Fernmelde.
Corvanta Corporate Colours
Orange:
Pantone 021C
R: 237 / G: 110 / B: 0
C: 0 / M: 53 / Y: 100 / K: 0
Hex #ED6E00
Dark Blue:
Pantone 662C
R: 15 / G: 31 / B: 122
C: 100 / M: 71 / Y: 0 / K:0
Hex #0F1F7A
Light Blue:
Pantone 300C
R: 0 / G: 110 / B: 199
C: 100 / M: 44 / Y: 0 / K:0
Hex #006EC7
Corvanta Corporate Fonts
The preferred font is Tahoma for Title, Topics and Print. In certain situations, Arial is an acceptable alternative.
Target Market(s)
Manufacturing industry, Automotive and Aerospace
Industry/Entity Type
Telecommunications
Look and feel
Each slider illustrates characteristics of the customer's brand and the style your logo design should communicate.

```html
<!DOCTYPE html>
<html lang="en">
<head>
<meta charset="utf-8">
<title>Corvanta Slide Template</title>
<link rel="stylesheet" href="https://fonts.googleapis.com/css2?family=PT+Sans:wght@400;700&display=swap">
<style>
  :root {
    --navy: #1b2a7c;
    --rule: #1f3f7a;
    --dark-blue: #0058a6;
    --light-blue: #0078c8;
    --orange: #f5911e;
    --white: #ffffff;
    --text: #222222;
  }
  html, body {
    margin: 0;
    padding: 0;
    overflow: hidden;
    background: var(--white);
  }
  .slide {
    position: relative;
    width: 1200px;
    height: 900px;
    overflow: hidden;
    background: var(--white);
    font-family: "PT Sans", Tahoma, Arial, sans-serif;
  }
  .slide-title {
    position: absolute;
    left: 22px;
    top: 40px;
    margin: 0;
    font-size: 36px;
    line-height: 1.1;
    font-weight: 700;
    color: var(--navy);
    letter-spacing: 0.6px;
  }
  .brand {
    position: absolute;
    right: 26px;
    top: 38px;
    display: flex;
    align-items: center;
    gap: 10px;
  }
  .brand-dot {
    width: 36px;
    height: 36px;
    border-radius: 50%;
    background: var(--orange);
  }
  .brand-name {
    font-size: 38px;
    font-weight: 700;
    color: var(--dark-blue);
    line-height: 1;
  }
  .header-rule {
    position: absolute;
    left: 0;
    top: 90px;
    width: 1200px;
    height: 2px;
    background: var(--rule);
  }
  .imagery-band {
    position: absolute;
    left: 2px;
    top: 586px;
    width: 1196px;
    height: 255px;
    background: linear-gradient(100deg, var(--dark-blue) 0%, var(--light-blue) 45%, #6f8ea6 70%, var(--orange) 100%);
    clip-path: polygon(1025px 0, 1196px 0, 1196px 255px, 0 255px, 0 170px, 769px 170px, 769px 85px, 1025px 85px);
  }
  .footer-rule {
    position: absolute;
    left: 0;
    top: 847px;
    width: 1200px;
    height: 2px;
    background: var(--rule);
  }
  .page-number {
    position: absolute;
    left: 590px;
    top: 862px;
    font-size: 15px;
    font-weight: 700;
    color: var(--text);
  }
  .footer-note {
    position: absolute;
    left: 775px;
    top: 866px;
    font-size: 15px;
    font-weight: 700;
    letter-spacing: 0.7px;
    color: var(--text);
    white-space: nowrap;
  }
</style>
</head>
<body>
<div class="slide">
  <h1 class="slide-title">Heading 1</h1>
  <div class="brand">
    <span class="brand-dot"></span>
    <span class="brand-name">Corvanta</span>
  </div>
  <div class="header-rule"></div>

  <div class="imagery-band" role="img" aria-label="Stepped band of brand-coloured squares and industry photographs: transport, city, technicians, circuitry, aircraft and construction"></div>

  <div class="footer-rule"></div>
  <div class="page-number">2</div>
  <div class="footer-note">— © 2012 Corvanta Confidential &amp; Proprietary —</div>
</div>
</body>
</html>
```